Web interface for PC desktop app

We need an HTML design for our new PC software.

To get an idea of the project scope, please review the interface draft in the attached files. The screenshot shows almost all dialogs of our product.

Our product is software that allows users to replace static Windows wallpaper with live animated scenes. The program interface consists of a gallery where users can select and download animated scenes, as well as an information area with scene details and current desktop settings. The product will be distributed on the Vexlo platform among the gamer community.

For this project, you need to create an engaging and user-friendly interface using HTML and CSS in two color schemes (black and white). Additionally, you will need to create a colorized version of the main program icon in vector format (a draft of the program icon is attached), design all other program icons, including icons for the title bar, and redraw all other images according to your design style.

Project Requirements:
-Develop a comprehensive design for the application, including icons and images, in two color schemes: dark and light.
-Colorize our main program icon according to your design style.
-Create other UI icons in all sizes from 16x16 to 512x512 pixels, ensuring that other images are suitable for up to 4K monitors.
-Ensure all UI controls have styles for standard Windows states: normal, hovered, active, and disabled.

Deliverables:
-Final design in HTML and CSS format.
-Icons in ICO format.
-Images in PNG format.

• all interface elements, including the program title bar, coded in HTML and CSS.

```html
<!DOCTYPE html>
<html lang="en">
<head>
<meta charset="utf-8">
<title>Display Settings</title>
<link href="https://fonts.googleapis.com/css2?family=Inter:wght@400;500;600;700&display=swap" rel="stylesheet">
<style>
:root{
  --bg:#0b0b0b;
  --modal:#0f0f0f;
  --card:#121212;
  --line:#262626;
  --text:#f2f2f2;
  --muted:#8a8a8a;
  --accent:#29b8f6;
  --danger-bg:#1f1515;
  --tab-bg:#161616;
}
*{box-sizing:border-box;margin:0;padding:0}
html,body{width:1200px;height:675px;overflow:hidden;background:var(--bg);font-family:"Inter",sans-serif;color:var(--text)}
.app{position:relative;width:1200px;height:675px;overflow:hidden}
.backdrop{position:absolute;inset:0;filter:blur(6px);opacity:.55}
.bg-pill{position:absolute;left:44px;top:44px;width:153px;height:29px;border-radius:15px;background:#1d6f93}
.bg-label{position:absolute;font-size:8px;color:#777}
.bg-panel{position:absolute;border-radius:12px;background:#151515}
.scene{position:absolute;border-radius:14px}
.scene-a{left:850px;top:193px;width:180px;height:120px;background:linear-gradient(180deg,#5a3a4a,#b45a3a 70%,#3a2a30)}
.scene-b{left:1050px;top:193px;width:100px;height:120px;background:linear-gradient(180deg,#a8452e,#d17a3a 60%,#4a2a2a)}
.scene-c{left:868px;top:370px;width:290px;height:160px;background:linear-gradient(180deg,#a43f3a,#4a3e6a 45%,#1e3a6a)}
.scene-d{left:868px;top:550px;width:290px;height:130px;background:linear-gradient(180deg,#7a4a2a,#3a2a1e)}
.scene-e{left:760px;top:370px;width:90px;height:220px;background:linear-gradient(180deg,#b4683a,#5a3a2a)}
.scene-f{left:62px;top:306px;width:290px;height:126px;background:linear-gradient(180deg,#1e2a4a,#3a4a2a 60%,#5a3a1e)}
.scene-g{left:62px;top:110px;width:118px;height:70px;background:linear-gradient(135deg,#1e2e5a,#5a2a2a)}
.scene-h{left:234px;top:110px;width:118px;height:70px;background:linear-gradient(135deg,#1e3a2a,#3a1e2a)}
.scrim{position:absolute;inset:0;background:rgba(0,0,0,.45)}

.modal{position:absolute;left:419px;top:36px;width:362px;height:603px;background:var(--modal);border:1px solid #222;border-radius:16px}
.modal-title{position:absolute;left:18px;top:16px;font-size:9.4px;font-weight:500}
.modal-close{position:absolute;right:18px;top:16px;font-size:9.4px;color:var(--accent)}
.tabs{position:absolute;left:18px;top:44px;width:325px;height:29px;border-radius:15px;background:var(--tab-bg);display:flex}
.tab{flex:1;display:flex;align-items:center;justify-content:center;gap:6px;font-size:9.4px;border-radius:15px}
.tab.active{background:var(--accent)}
.tab svg{width:12px;height:12px}
.card{position:absolute;left:18px;width:325px;background:var(--card);border:1px solid var(--line);border-radius:15px}
.card-title{position:absolute;left:18px;font-size:12.5px;font-weight:600}
.card-rule{position:absolute;left:18px;right:18px;height:1px;background:var(--line)}
.field-label{position:absolute;font-size:9px;color:var(--muted)}
.field-value{position:absolute;font-size:9px}
.option{position:absolute;left:18px;display:flex;align-items:center;gap:7px;font-size:9px}
.radio{width:15px;height:15px;border-radius:50%;border:1px solid #2a2a2a;background:#161616;flex:none}
.note{position:absolute;left:18px;right:18px;font-size:8.9px;line-height:11.3px;color:#777}
.dual-label{position:absolute;left:18px;top:547px;font-size:9px;color:var(--muted)}
.btn{position:absolute;top:555px;height:29px;border-radius:15px;display:flex;align-items:center;gap:10px;padding-left:4px;font-size:9.4px;border:1px solid #262626}
.btn-icon{width:21px;height:21px;border-radius:50%;display:flex;align-items:center;justify-content:center;background:#181818}
.btn-save{left:180px;width:72px;background:#121212}
.btn-cancel{left:264px;width:80px;background:var(--danger-bg);border-color:#2a1a1a}
.btn-cancel .btn-icon{background:#2a1c1c}
</style>
</head>
<body>
<div class="app">
  <div class="backdrop" aria-hidden="true">
    <div class="bg-pill"></div>
    <div class="bg-label" style="left:108px;top:55px;color:#cde">Wallpaper</div>
    <div class="bg-label" style="left:270px;top:55px">Downloads</div>
    <div class="bg-label" style="left:1026px;top:36px">Settings</div>
    <div class="bg-label" style="left:1120px;top:36px">Account</div>
    <div class="bg-label" style="left:826px;top:102px">Category</div>
    <div class="bg-label" style="left:1074px;top:102px">Top Rated</div>
    <div class="bg-label" style="left:150px;top:611px">Create your own wallpaper</div>
    <div class="bg-panel" style="left:44px;top:92px;width:150px;height:145px"></div>
    <div class="bg-panel" style="left:44px;top:280px;width:320px;height:300px"></div>
    <div class="scene scene-g" role="img" aria-label="Pixel city scene thumbnail"></div>
    <div class="scene scene-h" role="img" aria-label="Pixel forest scene thumbnail"></div>
    <div class="scene scene-f" role="img" aria-label="Selected pixel city scene preview"></div>
    <div class="scene scene-a" role="img" aria-label="Pixel sunset city scene"></div>
    <div class="scene scene-b" role="img" aria-label="Pixel orange sky scene"></div>
    <div class="scene scene-c" role="img" aria-label="Pixel skyline at dusk scene"></div>
    <div class="scene scene-d" role="img" aria-label="Pixel street scene"></div>
    <div class="scene scene-e" role="img" aria-label="Pixel sunset scene"></div>
  </div>
  <div class="scrim"></div>

  <section class="modal" aria-label="Display Settings">
    <div class="modal-title">Display Settings</div>
    <div class="modal-close">X Close</div>

    <div class="tabs">
      <div class="tab active">
        <svg viewBox="0 0 24 24" fill="none" stroke="#fff" stroke-width="1.8"><rect x="3" y="4" width="18" height="12" rx="2"/><path d="M9 20h6M12 16v4"/></svg>
        Monitor 1
      </div>
      <div class="tab">
        <svg viewBox="0 0 24 24" fill="none" stroke="#fff" stroke-width="1.8"><rect x="3" y="4" width="18" height="12" rx="2"/><path d="M9 20h6M12 16v4"/></svg>
        Monitor 2
      </div>
    </div>

    <div class="card" style="top:91px;height:142px">
      <div class="card-title" style="top:15px">Video Adapter</div>
      <div class="card-rule" style="top:46px"></div>
      <div class="field-label" style="left:18px;top:63px">Name</div>
      <div class="field-value" style="left:18px;top:79px">Nexora (R) VX Graphics 740</div>
      <div class="field-label" style="left:160px;top:63px">Rendering</div>
      <div class="field-value" style="left:160px;top:79px">HAL</div>
      <div class="option" style="top:106px"><span class="radio"></span>Disable hardware 3D rendering</div>
    </div>

    <div class="card" style="top:251px;height:130px">
      <div class="card-title" style="top:15px">Monitor Usage</div>
      <div class="card-rule" style="top:46px"></div>
      <div class="option" style="top:66px"><span class="radio"></span>Display screen saver on this monitor</div>
      <div class="option" style="top:90px"><span class="radio"></span>Display nothing on this monitor</div>
    </div>

    <div class="card" style="top:400px;height:131px">
      <div class="card-title" style="top:15px">Display Mode</div>
      <div class="card-rule" style="top:46px"></div>
      <div class="field-value" style="left:18px;top:67px">Display mode for this adapter:</div>
      <div class="note" style="top:91px">Note: The automatic display mode finds a mode that works well with your current screen saver settings and video adapter.</div>
    </div>

    <div class="dual-label">Dual Monitor Settings</div>
    <div class="option" style="top:569px"><span class="radio"></span>Show images in reverse order</div>

    <div class="btn btn-save">
      <span class="btn-icon"><svg width="10" height="10" viewBox="0 0 24 24" fill="none" stroke="#fff" stroke-width="2.4"><path d="M5 12l5 5 9-10"/></svg></span>Save
    </div>
    <div class="btn btn-cancel">
      <span class="btn-icon"><svg width="9" height="9" viewBox="0 0 24 24" fill="none" stroke="#fff" stroke-width="2.4"><path d="M5 5l14 14M19 5L5 19"/></svg></span>Cancel
    </div>
  </section>
</div>
</body>
</html>
```